body balm label design

body balm tube design, current label design for other similar products
Need to have a design which can interchange between 3 different solutions
Amber Tide (Lavender + Vanilla)
Copper Harbor (Eucalyptus + Mint)
Velvet Arc (Bergamot + Cedarwood)
Tube size:
2.5h x 3.25 w
Target Market(s)
natural, solution focused
Requirements
Must have
- relatable to existing brand designs, focus on features and benefits

```html
<!DOCTYPE html>
<html lang="en">
<head>
<meta charset="utf-8">
<title>Salt Calm Label Range</title>
<link rel="stylesheet" href="https://fonts.googleapis.com/css2?family=Cinzel:wght@400&family=Montserrat:wght@400;500&display=swap">
<style>
  :root {
    --canvas: #f3f1ee;
    --label-white: #ffffff;
    --plum: #7b2f85;
    --plum-text: #7e3b8c;
    --plum-rule: #9a5aa5;
    --ink: #2a2a2a;
  }
  * { box-sizing: border-box; margin: 0; padding: 0; }
  html, body { width: 1200px; height: 1200px; overflow: hidden; }
  body { background: var(--canvas); font-family: "Montserrat", sans-serif; }

  .range { position: relative; width: 1200px; height: 1200px; }

  .label {
    position: absolute;
    top: 260px;
    width: 300px;
    height: 680px;
    background: var(--label-white);
    overflow: hidden;
    box-shadow: 0 6px 24px rgba(0,0,0,0.12);
  }
  .label--amber { left: 50px; }
  .label--copper { left: 450px; }
  .label--velvet { left: 850px; }

  .label__top-art {
    position: absolute;
    top: 0; left: 0;
    width: 300px;
    height: 150px;
  }
  .label--amber .label__top-art {
    background: linear-gradient(180deg, #efe9d8 0%, #e6dcc4 40%, #c9b89e 55%, #f6f2ea 80%, #ffffff 100%);
  }
  .label--copper .label__top-art {
    background: linear-gradient(180deg, #3f9a3a 0%, #6cc04a 45%, #b9e0a0 75%, #ffffff 100%);
  }
  .label--velvet .label__top-art {
    background: linear-gradient(180deg, #8a6747 0%, #a9825e 40%, #d8c6b2 75%, #ffffff 100%);
  }

  .brand {
    position: absolute;
    top: 170px; left: 0;
    width: 300px;
    display: flex;
    justify-content: center;
    align-items: center;
    gap: 7px;
  }
  .brand__dot {
    width: 7px; height: 7px;
    border-radius: 50%;
    background: var(--ink);
  }
  .brand__name {
    font-family: "Montserrat", sans-serif;
    font-weight: 500;
    font-size: 15px;
    letter-spacing: 1px;
    color: var(--ink);
  }

  .product {
    position: absolute;
    top: 214px; left: 0;
    width: 300px;
    text-align: center;
  }
  .product__name {
    font-family: "Cinzel", serif;
    font-weight: 400;
    font-size: 32px;
    color: var(--plum-text);
    line-height: 1;
  }
  .product__subline {
    display: inline-block;
    margin-top: 10px;
    padding-bottom: 3px;
    border-bottom: 1px solid var(--plum-rule);
    font-size: 14px;
    color: var(--plum-text);
  }
  .product__detail {
    margin-top: 10px;
    font-size: 12px;
    line-height: 1.6;
    color: var(--plum-text);
  }

  .label__bottom-art {
    position: absolute;
    top: 390px; left: 0;
    width: 300px;
    height: 290px;
  }
  .label--amber .label__bottom-art {
    background: linear-gradient(160deg, #a07ac4 0%, #6a3c98 40%, #7b52a8 70%, #4e3a5a 100%);
  }
  .label--copper .label__bottom-art {
    background: linear-gradient(160deg, #8fa9a0 0%, #56706a 40%, #2f3f3a 75%, #6f8a82 100%);
  }
  .label--velvet .label__bottom-art {
    background: linear-gradient(160deg, #6fa83a 0%, #8cc04a 40%, #4f8a2a 70%, #a6d06a 100%);
  }

  .label__band {
    position: absolute;
    top: 346px; left: 0;
    width: 300px;
    height: 90px;
  }
  .band__shape { fill: var(--plum); }
  .band__edge { fill: none; stroke: #c9a8cf; stroke-width: 1.2; }
  .band__title {
    font-family: "Montserrat", sans-serif;
    font-weight: 500;
    font-size: 22px;
    letter-spacing: 4px;
    fill: #ffffff;
  }
  .band__title--long { font-size: 20px; letter-spacing: 3px; }
</style>
</head>
<body>
<main class="range">

  <article class="label label--amber">
    <div class="label__top-art" role="img" aria-label="Vanilla orchid blossoms and vanilla pods"></div>
    <div class="brand"><span class="brand__dot"></span><span class="brand__name">Terra Lune</span></div>
    <div class="product">
      <h2 class="product__name">SALT CALM</h2>
      <p class="product__subline">Lorem Ipsum Dolor Consectetuer</p>
      <p class="product__detail">Adipiscing Sed Elit<br>Diam Nonummy Euismod</p>
    </div>
    <div class="label__bottom-art" role="img" aria-label="Field of flowering lavender"></div>
    <svg class="label__band" viewBox="0 0 300 90">
      <path class="band__shape" d="M0 20 Q150 -14 300 20 L300 68 Q150 34 0 68 Z"/>
      <path class="band__edge" d="M0 68 Q150 34 300 68"/>
      <path id="arc-amber" d="M10 52 Q150 18 290 52" fill="none"/>
      <text class="band__title"><textPath href="#arc-amber" startOffset="50%" text-anchor="middle">AMBER TIDE</textPath></text>
    </svg>
  </article>

  <article class="label label--copper">
    <div class="label__top-art" role="img" aria-label="Fresh mint leaves"></div>
    <div class="brand"><span class="brand__dot"></span><span class="brand__name">Terra Lune</span></div>
    <div class="product">
      <h2 class="product__name">SALT CALM</h2>
      <p class="product__subline">Lorem Ipsum Dolor Consectetuer</p>
      <p class="product__detail">Adipiscing Sed Elit<br>Diam Nonummy Euismod</p>
    </div>
    <div class="label__bottom-art" role="img" aria-label="Eucalyptus leaves with dew drops"></div>
    <svg class="label__band" viewBox="0 0 300 90">
      <path class="band__shape" d="M0 20 Q150 -14 300 20 L300 68 Q150 34 0 68 Z"/>
      <path class="band__edge" d="M0 68 Q150 34 300 68"/>
      <path id="arc-copper" d="M6 52 Q150 18 294 52" fill="none"/>
      <text class="band__title band__title--long"><textPath href="#arc-copper" startOffset="50%" text-anchor="middle">COPPER HARBOR</textPath></text>
    </svg>
  </article>

  <article class="label label--velvet">
    <div class="label__top-art" role="img" aria-label="Cedar cones and pine needles"></div>
    <div class="brand"><span class="brand__dot"></span><span class="brand__name">Terra Lune</span></div>
    <div class="product">
      <h2 class="product__name">SALT CALM</h2>
      <p class="product__subline">Lorem Ipsum Dolor Consectetuer</p>
      <p class="product__detail">Adipiscing Sed Elit<br>Diam Nonummy Euismod</p>
    </div>
    <div class="label__bottom-art" role="img" aria-label="Whole and halved bergamot fruits"></div>
    <svg class="label__band" viewBox="0 0 300 90">
      <path class="band__shape" d="M0 20 Q150 -14 300 20 L300 68 Q150 34 0 68 Z"/>
      <path class="band__edge" d="M0 68 Q150 34 300 68"/>
      <path id="arc-velvet" d="M10 52 Q150 18 290 52" fill="none"/>
      <text class="band__title"><textPath href="#arc-velvet" startOffset="50%" text-anchor="middle">VELVET ARC</textPath></text>
    </svg>
  </article>

</main>
</body>
</html>
```